Veterinary Clinic Letterhead - Ridgeview Veterinary Surgery

We need a letterhead design for an established Veterinary Clinic in Mareeba called Ridgeview Veterinary Surgery. We are a moderate sized mixed animal veterinary clinic offering a wide variety of veterinary services. The design should use the same colour pattern as those in the logos supplied. The design should also include our address (48 Tulloch Road, Brindle Creek, Queensland, 4893), phone number (07 4158 6734), email (admin@ridgeviewvets.com.au), website (www.ridgeviewvets.com.au) and our opening hours (8am to 5pm Monday to Friday and 8am to 12pm Saturday).
Target Market(s)
Pet owners
Industry/Entity Type
Veterinary
Requirements
Must have
- The logo or modification of it, business address, opening hours, website, phone number and email address

```html
<!DOCTYPE html>
<html lang="en">
<head>
<meta charset="utf-8">
<title>Ridgeview Veterinary Surgery – Letterhead</title>
<link rel="stylesheet" href="https://fonts.googleapis.com/css2?family=Open+Sans:wght@400;600;700&family=Raleway:wght@400;600;700&display=swap">
<style>
  :root {
    --navy: #0f2a4f;
    --ink: #3a3a3a;
    --body: #6e6e6e;
    --muted: #7a7a7a;
    --desk: #e6e7ea;
    --paper: #ffffff;
  }
  * { box-sizing: border-box; margin: 0; padding: 0; }
  html, body { width: 968px; height: 1200px; overflow: hidden; background: var(--desk); }
  .letterhead {
    position: absolute; left: 69px; top: 18px;
    width: 830px; height: 1164px;
    background: var(--paper);
    overflow: hidden;
    box-shadow: 0 4px 14px rgba(0,0,0,.18);
    font-family: "Open Sans", sans-serif;
  }
  .brand-name {
    position: absolute; left: 46px; top: 142px;
    font-family: "Raleway", sans-serif; font-weight: 600; font-size: 15px;
    color: var(--navy); line-height: 1; letter-spacing: .3px;
  }
  .header-rule {
    position: absolute; left: 46px; top: 167px; width: 464px; height: 1px;
    background: var(--navy);
  }
  .contact-list {
    position: absolute; left: 513px; top: 97px; list-style: none;
    font-family: "Raleway", sans-serif; font-size: 12.8px; color: var(--muted);
  }
  .contact-list li { display: flex; align-items: center; height: 19.6px; }
  .contact-list svg { width: 10px; height: 10px; margin-right: 5px; flex: none; }
  .recipient { position: absolute; left: 66px; top: 312px; }
  .recipient .name { font-size: 17px; font-weight: 700; color: var(--ink); line-height: 1.2; }
  .recipient .role { font-size: 12px; color: var(--muted); margin-top: 3px; }
  .letter-date {
    position: absolute; right: 66px; top: 356px;
    font-size: 12px; color: var(--ink);
  }
  .letter-body {
    position: absolute; left: 66px; top: 401px; width: 698px;
    font-size: 12px; line-height: 17.4px; letter-spacing: .3px; color: var(--body);
    text-align: justify;
  }
  .letter-body p + p { margin-top: 17.4px; }
  .signature-art {
    position: absolute; left: 66px; top: 849px; width: 148px; height: 30px;
    background: linear-gradient(90deg, #d9dce2, #eceef1);
  }
  .signatory { position: absolute; left: 66px; top: 881px; }
  .signatory .name { font-family: "Raleway", sans-serif; font-weight: 700; font-size: 16px; color: var(--ink); }
  .signatory .role { font-size: 12px; color: var(--muted); margin-top: 2px; }
  .hours-band {
    position: absolute; left: 0; top: 1104px; width: 672px; height: 46px;
    background: var(--navy);
    clip-path: polygon(0 0, 657px 0, 672px 100%, 0 100%);
    display: flex; align-items: center; padding-left: 36px;
    font-family: "Raleway", sans-serif; font-size: 14.5px; color: #fff;
  }
  .hours-band strong { font-weight: 700; margin-right: 4px; }
</style>
</head>
<body>
  <main class="letterhead">
    <p class="brand-name">RIDGEVIEW VETERINARY SURGERY</p>
    <div class="header-rule"></div>

    <ul class="contact-list">
      <li><svg viewBox="0 0 10 10"><circle cx="5" cy="5" r="5" fill="#0f2a4f"/><path d="M3.2 2.6l1 .9-.5.8c.4.8 1 1.4 1.8 1.8l.8-.5.9 1-.7.8C4.6 7.2 2.8 5.4 2.4 3.3z" fill="#fff"/></svg>07 4158 6734</li>
      <li><svg viewBox="0 0 10 10"><circle cx="5" cy="5" r="5" fill="#0f2a4f"/><rect x="2.4" y="3.3" width="5.2" height="3.6" fill="#fff"/><path d="M2.4 3.3L5 5.3l2.6-2" stroke="#0f2a4f" stroke-width=".6" fill="none"/></svg>admin@ridgeviewvets.com.au</li>
      <li><svg viewBox="0 0 10 10"><circle cx="5" cy="5" r="4.4" fill="none" stroke="#0f2a4f" stroke-width="1"/><ellipse cx="5" cy="5" rx="1.8" ry="4.4" fill="none" stroke="#0f2a4f" stroke-width=".7"/><path d="M.8 5h8.4M1.5 3h7M1.5 7h7" stroke="#0f2a4f" stroke-width=".6"/></svg>www.ridgeviewvets.com.au</li>
      <li><svg viewBox="0 0 10 10"><circle cx="5" cy="5" r="5" fill="#0f2a4f"/><path d="M5 2.2a2 2 0 0 1 2 2c0 1.4-2 3.6-2 3.6S3 5.6 3 4.2a2 2 0 0 1 2-2z" fill="#fff"/><circle cx="5" cy="4.2" r=".7" fill="#0f2a4f"/></svg>48 Tulloch Road, Brindle Creek, Queensland, 4893</li>
    </ul>

    <section class="recipient">
      <p class="name">Name Surname</p>
      <p class="role">Senior Executive</p>
    </section>
    <p class="letter-date">Date, 10 September, 2030</p>

    <section class="letter-body">
      <p>Lorem ipsum dolor sit amet, consectetur adipisicing elit, sed do eiusmod tempor incididunt ut labore et dolore magna aliqua. Ut enim ad minim veniam, quis nostrud exercitation ullamco laboris nisi ut aliquip ex ea commodo consequat. Duis aute irure dolor in reprehenderit in voluptate velit esse cillum dolore eu fugiat nulla pariatur. Excepteur sint occaecat cupidatat non proident, sunt in culpa qui officia deserunt mollit anim id est laborum. Sed ut perspiciatis unde omnis iste natus error sit voluptatem accusantium doloremque laudantium, totam rem aperiam, eaque ipsa quae ab illo inventore veritatis et quasi architecto beatae vitae dicta sunt explicabo. Nemo enim ipsam voluptatem quia voluptas sit aspernatur aut odit aut fugit, sed quia consequuntur magni dolores eos qui ratione voluptatem sequi nesciunt. Neque porro voluptatem sequi nesciunt. Nemo enim ipsam voluptatem quia voluptas.</p>
      <p>Lorem ipsum dolor sit amet, consectetur adipisicing elit, sed do eiusmod tempor incididunt ut labore et dolore magna aliqua. Ut enim ad minim veniam, quis nostrud exercitation ullamco laboris nisi ut aliquip ex ea commodo consequat. Duis aute irure dolor in reprehenderit in voluptate velit esse cillum dolore eu fugiat nulla pariatur. Excepteur sint occaecat cupidatat non proident, sunt in culpa qui officia deserunt mollit anim id est laborum. Sed ut perspiciatis unde omnis iste natus error sit voluptatem accusantium doloremque laudantium, totam rem aperiam, eaque ipsa quae ab illo inventore veritatis et quasi architecto beatae vitae dicta sunt explicabo. Nemo enim ipsam voluptatem quia voluptas sit aspernatur aut odit aut.</p>
      <p>Lorem ipsum dolor sit amet, consectetur adipisicing elit, sed do eiusmod tempor incididunt ut labore et dolore magna aliqua. Ut enim ad minim veniam, quis nostrud exercitation ullamco laboris nisi ut aliquip ex ea commodo consequat.ua. Ut enim ad minim veniam, quis nostrud exercitation ullamco laboris nisi ut aliquip ex ea commodo consequat. Duis aute irure dolor in reprehenderit in voluptate velit esse cillum dolore eu fugiat nulla pariatur. Excepteur sint occaecat cupidatat non proident, sunt in culpa qui officia deserunt mollit anim id est laborum. Sed ut perspiciatis unde omnis iste natus error sit voluptatem accusantium doloremque laudantium, totam rem aperiam, eaque ipsa quae ab illo inventore veritatis et quasi architecto beatae vitae dicta sunt explicabo. Nemo enim ipsam voluptatem</p>
    </section>

    <div class="signature-art" role="img" aria-label="Handwritten signature of the general manager"></div>
    <section class="signatory">
      <p class="name">NAME SURNAME</p>
      <p class="role">General Manager</p>
    </section>

    <footer class="hours-band"><strong>OPENING HOURS</strong> (8am to 5pm Monday to Friday and 8am to 12pm Saturday).</footer>
  </main>
</body>
</html>
```